LumaVerge New Website

LumaVerge is a digital marketing agency. Our clients are all limousine companies. We need a responsive website designed to highlight our services and products. Our competition is http://www.clearpathgrowthhub.example/ and we need a site of similar design and layout without being too similar. Our old website www.lumaverge.example, is very outdated and the logo and graphics have changed. We will adjust the content to work with the new design. The new logo is attached.

```html
<!DOCTYPE html>
<html lang="en">
<head>
<meta charset="utf-8">
<title>LumaVerge – Contact Us</title>
<link rel="stylesheet" href="https://fonts.googleapis.com/css2?family=Open+Sans:wght@300;400;600;700;800&display=swap">
<style>
:root{
  --navy:#063a5a;
  --navy-dark:#053451;
  --gold:#a08a1f;
  --ink:#3a3a3a;
  --muted:#6b6b6b;
  --line:#e3e3e3;
  --page:#ffffff;
  --band:#f7f7f7;
  --footer-text:#c9d6df;
  --footer-box:#0a4d73;
}
*{box-sizing:border-box;margin:0;padding:0}
html,body{width:848px;height:1200px;overflow:hidden;background:var(--page);font-family:"Open Sans",sans-serif;color:var(--ink)}
.canvas{position:relative;width:848px;height:1200px;overflow:hidden}
.site-header{position:absolute;top:0;left:0;width:848px;height:94px;background:var(--band);text-align:center}
.brand{padding-top:6px;font-size:35px;font-weight:300;color:var(--navy);letter-spacing:.5px;line-height:42px}
.tagline{font-size:7.5px;font-weight:600;color:#555;letter-spacing:.4px;margin-top:5px}
.header-contacts{display:flex;justify-content:center;gap:16px;margin-top:7px;font-size:9.5px;color:#555}
.header-contacts span{display:flex;align-items:center;gap:5px}
.main-nav{position:absolute;top:94px;left:0;width:848px;height:29px;background:var(--navy-dark);display:flex;justify-content:center}
.main-nav a{color:#fff;text-decoration:none;font-size:9px;line-height:29px;padding:0 12px;border-left:1px solid rgba(255,255,255,.08)}
.main-nav a:last-child{border-right:1px solid rgba(255,255,255,.08)}
.page-title{position:absolute;top:123px;left:0;width:848px;height:107px;background:var(--band);text-align:center;border-bottom:1px solid var(--line)}
.page-title h1{font-size:24px;font-weight:800;color:var(--navy);margin-top:17px;letter-spacing:.3px}
.title-rule{position:relative;width:678px;height:1px;background:var(--line);margin:9px auto 0}
.title-rule::after{content:"";position:absolute;left:50%;top:-1px;width:46px;height:2px;margin-left:-23px;background:var(--gold)}
.page-title p{font-size:10.5px;font-weight:600;color:#555;margin-top:15px}
.breadcrumb{position:absolute;top:230px;left:0;width:848px;height:30px;border-bottom:1px solid var(--line);padding-left:84px;font-size:8px;line-height:30px;color:#999}
.breadcrumb a{color:var(--gold);text-decoration:none}
.map{position:absolute;top:280px;left:85px;width:678px;height:140px;background:linear-gradient(100deg,#e9e5d8,#dfe5d2 45%,#e6e1d4 70%,#e9e5dc)}
.section-rule{position:absolute;top:445px;left:85px;width:678px;height:1px;background:var(--line)}
.section-rule::after{content:"";position:absolute;left:50%;top:-1px;width:46px;height:2px;margin-left:-23px;background:var(--gold)}
.section-heading{font-size:13.5px;font-weight:400;color:var(--gold);letter-spacing:.2px}
.contact-form{position:absolute;top:475px;left:85px;width:434px}
.form-grid{display:grid;grid-template-columns:209px 209px;column-gap:16px;row-gap:11px;margin-top:11px}
.field label{display:block;font-size:8px;color:#555;margin-bottom:6px}
.field .input{height:28px;border:1px solid #dcdcdc;background:#fff}
.field.wide{grid-column:1 / 3}
.field.wide .input{height:66px}
.submit{display:inline-block;margin-top:16px;width:96px;height:32px;background:var(--gold);color:#fff;font-size:9.5px;text-align:center;line-height:32px}
.contact-info{position:absolute;top:475px;left:544px;width:262px}
.contact-info p.lead{font-size:8.3px;line-height:15px;color:#888;margin-top:11px}
.info-row{display:flex;gap:10px;align-items:flex-start;margin-top:10px;font-size:8.5px;line-height:14px;color:#777}
.info-row svg{flex:none}
.welcome{margin-top:12px;font-size:10.5px;color:var(--navy)}
.site-footer{position:absolute;top:842px;left:0;width:848px;height:358px;background:var(--navy)}
.footer-heading{font-size:13.5px;font-weight:700;color:#fff;letter-spacing:.2px}
.useful{position:absolute;top:30px;left:85px}
.link-cols{display:flex;gap:36px;margin-top:14px}
.link-col{width:153px}
.link-col a{display:block;color:var(--footer-text);text-decoration:none;font-size:10px;line-height:16px;padding:5px 1px 6px;border-bottom:1px solid rgba(255,255,255,.08)}
.link-col a:last-child{border-bottom:none}
.follow{position:absolute;top:238px;left:86px;width:231px;height:38px;background:var(--footer-box);display:flex;align-items:center;padding-left:18px;gap:10px;font-size:10px;color:var(--footer-text)}
.follow i{display:block;width:14px;height:14px;border-radius:50%;background:#fff}
.blog{position:absolute;top:30px;left:502px;width:260px}
.post{display:flex;gap:10px;padding:12px 0 8px;border-bottom:1px solid rgba(255,255,255,.1)}
.post:last-child{border-bottom:none}
.date{flex:none;width:31px;height:30px;background:var(--footer-box);color:#fff;text-align:center;font-size:6.5px;line-height:9px;padding-top:3px;margin-top:4px}
.date b{display:block;font-size:15px;line-height:16px;font-weight:600}
.post p{font-size:10px;line-height:17px;color:var(--footer-text)}
.post a{display:block;color:#fff;font-size:10px;text-decoration:none;margin-top:7px}
.footer-bottom{position:absolute;top:307px;left:0;width:848px;height:51px;border-top:1px solid rgba(255,255,255,.08);display:flex;justify-content:space-between;align-items:center;padding:0 85px;font-size:7.5px;color:var(--footer-text);letter-spacing:.2px}
.footer-bottom nav span{margin:0 8px}
</style>
</head>
<body>
<div class="canvas">
  <header class="site-header">
    <div class="brand">lumaverge</div>
    <div class="tagline">CLEAR ROUTES. BRIGHT BRANDS.</div>
    <div class="header-contacts">
      <span><svg width="9" height="9" viewBox="0 0 10 10"><path d="M2 0.5 L4 2.8 L3 4 Q4 6 6 7 L7.2 6 L9.5 8 L8.3 9.5 Q2.5 9 0.5 1.7 Z" fill="#555"/></svg>555-014-2290</span>
      <span><svg width="10" height="8" viewBox="0 0 10 8"><rect x="0.5" y="0.5" width="9" height="7" fill="#555"/><path d="M0.5 0.5 L5 4.5 L9.5 0.5" stroke="#fff" fill="none" stroke-width=".8"/></svg>info@lumaverge.example</span>
    </div>
  </header>

  <nav class="main-nav">
    <a href="#">Home</a><a href="#">About Us</a><a href="#">Integrated Marketing</a><a href="#">Services</a><a href="#">News &amp; Events</a><a href="#">LoyalRoutes™</a><a href="#">Blog</a><a href="#">Contact Us</a>
  </nav>

  <section class="page-title">
    <h1>CONTACT US</h1>
    <div class="title-rule"></div>
    <p>WE ARE WAITING YOU TO GET IN TOUCH WITH US</p>
  </section>

  <div class="breadcrumb"><a href="#">Home</a> &nbsp;//&nbsp; Contact Us</div>

  <div class="map" role="img" aria-label="Street map showing the office location"></div>
  <div class="section-rule"></div>

  <section class="contact-form">
    <h2 class="section-heading">GET CONNECTED</h2>
    <div class="form-grid">
      <div class="field"><label>First Name (required)</label><div class="input"></div></div>
      <div class="field"><label>Last Name (required)</label><div class="input"></div></div>
      <div class="field"><label>Company</label><div class="input"></div></div>
      <div class="field"><label>Website</label><div class="input"></div></div>
      <div class="field"><label>Email (required)</label><div class="input"></div></div>
      <div class="field"><label>Phone (required)</label><div class="input"></div></div>
      <div class="field wide"><label>Message</label><div class="input"></div></div>
    </div>
    <div class="submit">SUBMIT NOW</div>
  </section>

  <aside class="contact-info">
    <h2 class="section-heading">CONTACT INFORMATION</h2>
    <p class="lead">Aliquam in dolor sollicitudin, ornare tortor et, convallis justo. Ut velit erat, dictum ut maximus vel, faucibus in dolor. Quisque lacinia ex nec placerat ultricies.</p>
    <div class="info-row" style="margin-top:14px">
      <svg width="14" height="16" viewBox="0 0 14 16"><path d="M7 15 C3 10 1.5 8 1.5 5.8 A5.5 5.5 0 0 1 12.5 5.8 C12.5 8 11 10 7 15Z" fill="none" stroke="var(--gold)" stroke-width="1"/><circle cx="7" cy="6" r="2" fill="none" stroke="var(--gold)"/></svg>
      <span>412 Harbor Lane S<br>Newport, NY 10099-0142</span>
    </div>
    <div class="info-row">
      <svg width="14" height="14" viewBox="0 0 14 14"><path d="M3 1 L5.5 4 L4.3 5.5 Q5.5 8.3 8.5 9.7 L10 8.5 L13 11 L11.3 13 Q3 12 1 2.6 Z" fill="none" stroke="var(--gold)"/></svg>
      <span>555-014-2290</span>
    </div>
    <div class="info-row">
      <svg width="15" height="11" viewBox="0 0 15 11"><rect x="0.5" y="0.5" width="14" height="10" fill="none" stroke="var(--gold)"/><path d="M0.5 0.5 L7.5 6.5 L14.5 0.5" fill="none" stroke="var(--gold)"/></svg>
      <span>info@lumaverge.example</span>
    </div>
    <div class="welcome">You are welcome !</div>
  </aside>

  <footer class="site-footer">
    <div class="useful">
      <h2 class="footer-heading">USEFUL LINKS</h2>
      <div class="link-cols">
        <div class="link-col">
          <a href="#">Home</a>
          <a href="#">Online Image &amp; Reputation Management</a>
          <a href="#">Blog</a>
          <a href="#">Customer Retention &amp;&nbsp; Loyalty</a>
          <a href="#">Mobile Marketing</a>
        </div>
        <div class="link-col">
          <a href="#">OutBound Marketing</a>
          <a href="#">Support to Complete the Sale</a>
          <a href="#">Social Media Marketing</a>
          <a href="#">InBound Marketing</a>
        </div>
      </div>
    </div>
    <div class="follow">Follow Us on :<i></i><i></i><i></i><i></i><i></i></div>

    <div class="blog">
      <h2 class="footer-heading">LATEST BLOG</h2>
      <div class="post"><div class="date">Dec<b>03</b></div><div><p>Maecenas purus neque, tincidunt sed urna a, maximus semper nisi ut vel libero.</p><a href="#">read more</a></div></div>
      <div class="post"><div class="date">Dec<b>03</b></div><div><p>Maecenas purus neque, tincidunt sed urna a, maximus semper nisi ut vel libero.</p><a href="#">read more</a></div></div>
      <div class="post"><div class="date">Dec<b>03</b></div><div><p>Maecenas purus neque, tincidunt sed urna a, maximus semper nisi ut vel libero.</p><a href="#">read more</a></div></div>
    </div>

    <div class="footer-bottom">
      <nav>TERMS<span>|</span>PRIVACY POLICY<span>|</span>TERMS AND CONDITIONS<span>|</span>SITEMAP</nav>
      <div>COPYRIGHT © 2015 LUMAVERGE. ALL RIGHTS RESERVED.</div>
    </div>
  </footer>
</div>
</body>
</html>
```